Halvorsen Partners Business Card

Halvorsen Partners Civil Construction
Marcus Halvorsen
CEO
727-518-6094
Marcus@HalvorsenSiteworks.example
www.HalvorsenSiteworks.example
Site Development
Utility Construction
Excavation
40876 County Lane 19
Land O' Lakes, FL 34638

Target Market(s)

Construction and government

Industry/Entity Type

Business

Contact Information for Business Card

I want an unique design that make a statement

Number of Pages Required

1 page

Font styles to use

Colors

Designer to choose colors to be used in the design.

Requirements
Must have
• unique design, feel free to modify or change the color of my logo.
Nice to have
• extra design features like spot UV, foil accents, color edges, unique paper, or any thing that would make my card pop.
• I like the feel of the image that I attached

```html
<!DOCTYPE html>
<html lang="en">
<head>
<meta charset="utf-8">
<title>Halvorsen Partners Business Card</title>
<link rel="stylesheet" href="https://fonts.googleapis.com/css2?family=Marcellus&family=Lato:wght@400&display=swap">
<style>
  :root {
    --backdrop: #1b1b1b;
    --slate: #6e6f72;
    --navy: #21407c;
    --paper: #f3f3f3;
    --paper-white: #f8f9fb;
    --ink: #151515;
  }
  * { margin: 0; padding: 0; box-sizing: border-box; }
  html, body { width: 1200px; height: 900px; overflow: hidden; background: var(--backdrop); }
  .stage { position: relative; width: 1200px; height: 900px; }

  .card { position: absolute; top: 170px; width: 347px; height: 560px; overflow: hidden; }

  /* Front */
  .card-front { left: 259px; background: var(--navy); }
  .front-header {
    height: 201px; background: var(--slate); color: #fff; text-align: center;
    font-family: "Marcellus", serif;
  }
  .holder-name { padding-top: 58px; font-size: 34px; letter-spacing: 0.5px; font-weight: 400; }
  .holder-title { margin-top: 12px; font-family: "Lato", sans-serif; font-size: 19px; }
  .front-brand {
    height: 359px; display: flex; flex-direction: column; align-items: flex-start;
    justify-content: flex-end; padding: 0 0 34px 30px; gap: 18px;
  }
  .front-brand .brand-square { width: 64px; height: 64px; background: var(--paper-white); }
  .front-brand .brand-name {
    font-family: "Marcellus", serif; color: var(--paper-white);
    font-size: 40px; line-height: 1.05; text-transform: uppercase;
  }

  /* Back */
  .card-back { left: 631px; background: var(--paper); text-align: center; }
  .brand-mark { width: 72px; height: 72px; background: var(--navy); margin: 270px auto 0; position: absolute; left: 137px; top: 0; margin: 0; top: 80px; }
  .company {
    position: absolute; left: 0; right: 0; top: 230px;
    font-family: "Marcellus", serif; color: var(--navy); font-weight: 400;
  }
  .company-name { font-size: 27px; letter-spacing: 0.5px; line-height: 1; }
  .company-line { font-size: 16px; letter-spacing: 4px; margin-top: 8px; line-height: 1; }

  .contact-icons { position: absolute; left: 0; right: 0; top: 346px; display: flex; justify-content: center; gap: 5px; }
  .contact-icons svg { width: 15px; height: 15px; }
  .contact-list {
    position: absolute; left: 0; right: 0; top: 372px; list-style: none;
    font-family: "Lato", sans-serif; font-size: 15px; line-height: 20px; color: var(--ink);
  }
  .divider { position: absolute; left: 58px; width: 230px; top: 455px; border: 0; border-top: 1px solid var(--navy); }
  .services {
    position: absolute; left: 0; right: 0; top: 477px;
    font-family: "Lato", sans-serif; font-size: 17px; line-height: 29px; color: var(--navy);
  }
  .services .sep { margin: 0 8px; }
</style>
</head>
<body>
<main class="stage">
  <section class="card card-front">
    <header class="front-header">
      <h1 class="holder-name">MARCUS HALVORSEN</h1>
      <p class="holder-title">CEO</p>
    </header>
    <div class="front-brand">
      <span class="brand-square"></span>
      <p class="brand-name">Halvorsen<br>Partners</p>
    </div>
  </section>

  <section class="card card-back">
    <span class="brand-mark"></span>
    <div class="company">
      <p class="company-name">HALVORSEN PARTNERS</p>
      <p class="company-line">CIVIL CONSTRUCTION</p>
    </div>

    <div class="contact-icons">
      <svg viewBox="0 0 16 16" aria-label="Phone"><path fill="#21407c" d="M3 1.5l2.5-.5 1.5 3.5-1.7 1.2a8 8 0 0 0 4.8 4.8l1.2-1.7 3.5 1.5-.5 2.5c-.3.8-1 1.2-2 1.1C7 13.2 2.8 9 1.9 3.5 1.8 2.5 2.2 1.8 3 1.5z"/></svg>
      <svg viewBox="0 0 16 16" aria-label="Email"><rect x="1" y="3" width="14" height="10" fill="#21407c"/><path d="M1.5 3.5L8 9l6.5-5.5" stroke="#f3f3f3" stroke-width="1.3" fill="none"/></svg>
      <svg viewBox="0 0 16 16" aria-label="Website"><circle cx="8" cy="8" r="7" fill="#21407c"/><path d="M5 4c2 1 1 3 3 3s1 3 3 4M10 3c-1 1 0 2 1 2" stroke="#f3f3f3" stroke-width="1.4" fill="none"/></svg>
    </div>
    <ul class="contact-list">
      <li>727-518-6094</li>
      <li>Marcus@HalvorsenSiteworks.example</li>
      <li>www.HalvorsenSiteworks.example</li>
    </ul>

    <hr class="divider">
    <div class="services">
      <p>Site Development<span class="sep">|</span>Utility Construction</p>
      <p>Excavation</p>
    </div>
  </section>
</main>
</body>
</html>
```